Whitlock Realty Corp needs a billboard design

We need to create a billboard for our company located in Radford, VA. Our company provides off-campus student housing for the students at Calder State College. We offer a variety of housing options (houses, town homes,apartments, and efficiencies) all of which are close to campus. Our properties come in 1, 2, 3, 4, and 5 bedroom options. Our company colors are burgundy, grey and white. we would like to push the idea of how close we are to campus. "Off-campus housing that not off the map" The billboard can be fun and geared to ages 17-25. There should also some connection to Calder State College.
The website should also be included whitlockleasing.example
Updates

i will add pictures to choose from.

Target Market(s)

college students

Industry/Entity Type

Real Estate

Font styles to use
Serif

Colors

Designer to choose colors to be used in the design.

Requirements
Must have
• company logo and website
• phone number 555-214-7308
• eye catching graphic not from our website. something new. if there are people there needs to be diversity.
Nice to have
• eye catching graphic that connects the viewer to Calder State College
• graphic could be a stylized map of the area showing properties close to campus
Should not have
• anything that could cause problems with fair housing laws

```html
<!DOCTYPE html>
<html lang="en">
<head>
<meta charset="utf-8">
<title>Whitlock Realty – Off-Campus Housing Billboard</title>
<link rel="stylesheet" href="https://fonts.googleapis.com/css2?family=Mulish:wght@300;400;800&family=Oswald:wght@500&display=swap">
<style>
  :root {
    --burgundy: #8a1c32;
    --grey: #b9b9bc;
    --ink: #2a2a2a;
    --bar: #262626;
    --white: #ffffff;
    --stage: #eeeeef;
  }
  html, body {
    margin: 0;
    width: 882px;
    height: 1200px;
    overflow: hidden;
    background: var(--stage);
  }
  .canvas {
    position: relative;
    width: 882px;
    height: 1200px;
  }
  .billboard {
    position: absolute;
    left: 20px;
    top: 390px;
    width: 938px;
    height: 468px;
    transform: scale(0.8977);
    transform-origin: 0 0;
    background: var(--white);
    overflow: hidden;
    box-shadow: 0 6px 18px rgba(0,0,0,.18);
    font-family: "Mulish", sans-serif;
  }
  .billboard-shapes {
    position: absolute;
    inset: 0;
  }
  .brand {
    position: absolute;
    left: 560px;
    width: 356px;
    top: 22px;
    text-align: center;
    color: var(--burgundy);
  }
  .brand-mark {
    width: 64px;
    height: 64px;
    margin: 0 auto 12px;
    border-radius: 50%;
    background: var(--burgundy);
  }
  .brand-name {
    font-family: "Mulish", sans-serif;
    font-weight: 800;
    font-size: 30px;
    letter-spacing: 6px;
    line-height: 30px;
    text-transform: uppercase;
  }
  .options {
    position: absolute;
    right: 30px;
    top: 192px;
    text-align: right;
    color: var(--white);
  }
  .options-lead {
    font-weight: 300;
    font-size: 34px;
    line-height: 36px;
  }
  .options-title {
    font-weight: 800;
    font-size: 38px;
    line-height: 40px;
    letter-spacing: .5px;
  }
  .options-list {
    font-weight: 400;
    font-size: 12.5px;
    line-height: 18px;
  }
  .campus-box {
    position: absolute;
    left: 527px;
    top: 326px;
    width: 381px;
    height: 50px;
    text-align: center;
  }
  .campus-title {
    position: absolute;
    left: 0; right: 0;
    top: -14px;
    margin: 0 auto;
    width: fit-content;
    padding: 0 10px;
    background: var(--white);
    font-weight: 800;
    font-size: 25px;
    line-height: 28px;
    color: var(--burgundy);
  }
  .campus-sizes {
    position: absolute;
    left: 0; right: 0;
    top: 22px;
    font-size: 18.5px;
    color: var(--ink);
  }
  .off-campus {
    position: absolute;
    left: 527px;
    width: 381px;
    top: 387px;
    display: flex;
    align-items: center;
    gap: 10px;
    font-family: "Oswald", sans-serif;
    font-weight: 500;
    font-size: 25px;
    line-height: 34px;
    color: var(--ink);
    white-space: nowrap;
  }
  .off-campus::before,
  .off-campus::after {
    content: "";
    flex: 1;
    height: 2px;
    background: var(--ink);
  }
  .contact-bar {
    position: absolute;
    left: 470px;
    right: 0;
    top: 427px;
    height: 36px;
    display: flex;
    align-items: center;
    justify-content: center;
    gap: 8px;
    color: var(--white);
    font-size: 19px;
  }
  .contact-bar svg { width: 18px; height: 18px; }
  .contact-phone {
    font-family: "Oswald", sans-serif;
    font-weight: 500;
    font-size: 22px;
  }
</style>
</head>
<body>
<main class="canvas">
  <section class="billboard">
    <svg class="billboard-shapes" viewBox="0 0 938 468" width="938" height="468">
      <defs>
        <linearGradient id="photo-tone" x1="0" y1="0" x2="1" y2="1">
          <stop offset="0" stop-color="#f1efec"/>
          <stop offset="0.45" stop-color="#d9c3b5"/>
          <stop offset="0.75" stop-color="#b8b7a6"/>
          <stop offset="1" stop-color="#7fae6f"/>
        </linearGradient>
      </defs>
      <path role="img" aria-label="Photo of four smiling, diverse college students standing together"
            d="M0 0 H463 C540 80 540 180 480 280 C440 345 430 410 445 468 H0 Z"
            fill="url(#photo-tone)"/>
      <path class="ribbon-grey" d="M455 0 C532 80 532 180 472 280 C432 345 422 410 437 468"
            fill="none" stroke="var(--grey)" stroke-width="7"/>
      <path class="ribbon-burgundy" d="M472 0 C549 80 549 180 489 280 C449 345 439 410 454 468"
            fill="none" stroke="var(--burgundy)" stroke-width="18"/>
      <rect class="options-band" x="478" y="186" width="460" height="116" fill="var(--burgundy)"/>
      <rect class="campus-frame" x="527" y="326" width="381" height="50" fill="none" stroke="var(--burgundy)" stroke-width="1.5"/>
      <rect class="contact-band" x="452" y="427" width="486" height="36" fill="var(--bar)"/>
    </svg>

    <div class="brand">
      <div class="brand-mark"></div>
      <div class="brand-name">Whitlock<br>Realty</div>
    </div>

    <div class="options">
      <div class="options-lead">A VARIETY OF</div>
      <div class="options-title">HOUSING OPTIONS</div>
      <div class="options-list">(HOUSES, TOWN HOMES,APARTMENTS, AND EFFICIENCIES)</div>
    </div>

    <div class="campus-box">
      <div class="campus-title">CLOSE TO CAMPUS</div>
      <div class="campus-sizes">1, 2, 3, 4, AND 5 BEDROOM OPTIONS</div>
    </div>

    <div class="off-campus">OFF-CAMPUS HOUSING</div>

    <div class="contact-bar">
      <svg viewBox="0 0 20 20" aria-hidden="true">
        <circle cx="10" cy="10" r="8.5" fill="none" stroke="#fff" stroke-width="1.5"/>
        <ellipse cx="10" cy="10" rx="3.8" ry="8.5" fill="none" stroke="#fff" stroke-width="1.2"/>
        <path d="M1.5 10 H18.5 M3 6 H17 M3 14 H17" stroke="#fff" stroke-width="1.1"/>
      </svg>
      <span class="contact-web">whitlockleasing.example</span>
      <span class="contact-divider">|</span>
      <svg viewBox="0 0 20 20" aria-hidden="true">
        <circle cx="10" cy="10" r="8.5" fill="none" stroke="#fff" stroke-width="1.5"/>
        <path d="M7 5.5 L8.6 7.6 L7.6 9 C8.3 10.5 9.5 11.7 11 12.4 L12.4 11.4 L14.5 13 L13.4 14.6 C9.5 14.2 5.8 10.5 5.4 6.6 Z" fill="#fff"/>
      </svg>
      <span class="contact-phone">555-214-7308</span>
    </div>
  </section>
</main>
</body>
</html>
```